The Jawline Remedy Business Card

Looking for a business card design: front and back. It will be printed at pressquill.example on a leaf cutout tricolumn paper with green middle. 3.5 x 2 leaf cutout. It will need bleed room around edges. The front will have my picture, logo, website and email address. The back will be a quote. "Finally. The complete solution to helping you open your mouth fully without pain"
and
"Like Us on Chirpbook to Learn More @ The Jawline Remedy"

Target Market(s)

Women 20-55 years old

Industry/Entity Type

Health Service

Contact Information for Business Card

My photo on one side or embedded, Name: Dr. Marlow Keddick, PT, DPT, MS Website: TheJawlineRemedy.example Email: marlow@brightpathcareclinic.example

Requirements
Must have
• Unique design consistent with my logo

```html
<!DOCTYPE html>
<html lang="en">
<head>
<meta charset="utf-8">
<title>The Jawline Remedy – Business Card</title>
<link rel="stylesheet" href="https://fonts.googleapis.com/css2?family=Poppins:wght@400;500;600;700&display=swap">
<style>
  :root {
    --stage: #2c2d2f;
    --brand-blue: #1f6fb8;
    --brand-green: #8cc63f;
    --paper: #ffffff;
    --photo-light: #c9dcf0;
    --photo-mid: #9fb9d6;
  }
  * { box-sizing: border-box; margin: 0; padding: 0; }
  html, body { width: 1200px; height: 900px; overflow: hidden; }
  body {
    background: var(--stage);
    font-family: "Poppins", sans-serif;
    position: relative;
  }
  .card {
    position: absolute;
    width: 700px;
    height: 400px;
    overflow: hidden;
    box-shadow: 0 10px 28px rgba(0,0,0,.45);
  }
  .card svg.card-art { position: absolute; inset: 0; width: 100%; height: 100%; }

  /* Back */
  .card-back { left: 70px; top: 40px; background: var(--brand-blue); }
  .quote {
    position: absolute;
    left: 60px; right: 60px; top: 80px;
    color: var(--paper);
    font-weight: 600;
    font-size: 27px;
    line-height: 1.35;
    text-align: center;
  }
  .quote .mark { color: var(--brand-green); font-size: 40px; line-height: 0; vertical-align: -12px; margin: 0 6px; }
  .social-line {
    position: absolute;
    right: 40px; bottom: 28px;
    display: flex; align-items: center; gap: 10px;
    color: var(--paper);
    font-size: 16px;
    font-weight: 500;
  }
  .social-line .square { width: 26px; height: 26px; background: var(--paper); }
  .social-line .small { font-size: 11px; display: block; line-height: 1; }
  .social-line .network { font-weight: 600; font-size: 19px; line-height: 1.05; }

  /* Front */
  .card-front { left: 430px; top: 470px; background: var(--paper); }
  .brand {
    position: absolute;
    right: 40px; top: 18px;
    display: flex; align-items: center; gap: 14px;
  }
  .brand .ring { width: 76px; height: 76px; border-radius: 50%; border: 6px solid var(--brand-blue); }
  .brand .name {
    color: var(--brand-green);
    font-weight: 700;
    font-size: 26px;
    line-height: 1.02;
  }
  .contact {
    position: absolute;
    right: 36px; bottom: 38px;
    text-align: right;
    color: var(--paper);
  }
  .contact .person { font-weight: 700; font-size: 17px; letter-spacing: .2px; }
  .contact .creds { color: var(--brand-green); font-weight: 500; }
  .contact .line { font-size: 15px; margin-top: 4px; display: flex; justify-content: flex-end; align-items: center; gap: 8px; }
  .contact svg { width: 15px; height: 15px; }
</style>
</head>
<body>

<section class="card card-back" aria-label="Card back">
  <svg class="card-art" viewBox="0 0 700 400" preserveAspectRatio="none" aria-hidden="true">
    <path d="M0 400 L0 360 C160 300 320 330 460 270 C570 225 640 190 700 180 L700 400 Z" fill="var(--brand-green)"/>
  </svg>
  <p class="quote"><span class="mark">&ldquo;</span>Finally. The complete solution to helping you open your mouth fully without pain<span class="mark">&rdquo;</span></p>
  <div class="social-line">
    <span class="square"></span>
    <span><span class="small">Like us on</span><span class="network">Chirpbook</span></span>
    <span>to Learn More @ The Jawline Remedy</span>
  </div>
</section>

<section class="card card-front" aria-label="Card front">
  <svg class="card-art" viewBox="0 0 700 400" preserveAspectRatio="none">
    <defs>
      <linearGradient id="portraitTone" x1="0" y1="0" x2="0" y2="1">
        <stop offset="0" stop-color="var(--photo-mid)"/>
        <stop offset="1" stop-color="var(--photo-light)"/>
      </linearGradient>
    </defs>
    <rect class="portrait" x="30" y="90" width="260" height="270" fill="url(#portraitTone)" role="img" aria-label="Portrait photo of Dr. Marlow Keddick in shirt and tie"/>
    <path d="M0 298 C150 338 250 310 315 240 C410 150 555 112 700 100 L700 400 L0 400 Z" fill="var(--brand-green)"/>
    <path d="M0 315 C150 355 258 326 322 256 C415 165 558 126 700 114 L700 400 L0 400 Z" fill="var(--paper)"/>
    <path d="M0 330 C150 370 262 340 330 270 C420 180 560 140 700 128 L700 400 L0 400 Z" fill="var(--brand-blue)"/>
  </svg>
  <div class="brand">
    <span class="ring"></span>
    <span class="name">The<br>Jawline<br>Remedy</span>
  </div>
  <div class="contact">
    <p class="person">DR. MARLOW KEDDICK, <span class="creds">PT, DPT, MS</span></p>
    <p class="line">marlow@brightpathcareclinic.example
      <svg viewBox="0 0 16 16" aria-hidden="true"><rect x="1" y="3" width="14" height="10" fill="none" stroke="var(--brand-green)" stroke-width="1.6"/><path d="M1 3 L8 9 L15 3" fill="none" stroke="var(--brand-green)" stroke-width="1.6"/></svg>
    </p>
    <p class="line">www.TheJawlineRemedy.example
      <svg viewBox="0 0 16 16" aria-hidden="true"><circle cx="8" cy="8" r="6.5" fill="none" stroke="var(--brand-green)" stroke-width="1.5"/><ellipse cx="8" cy="8" rx="3" ry="6.5" fill="none" stroke="var(--brand-green)" stroke-width="1.2"/><path d="M1.5 8 H14.5" stroke="var(--brand-green)" stroke-width="1.2"/></svg>
    </p>
  </div>
</section>

</body>
</html>
```